HCA Twirl under our moonbeams

My nonprofit social service agency is having a fun gala based on the TV show twirl under moonbeams, and we need the key design for an invitation. The event is a dinner and will have 7 local well-known people dance in a contest-like setting with a nationally known host. This does not need to be the final invitation (RSVP, list of dancers/hosts, etc.). All I need at this point is a great design for the cover to give this event an identity and entice people to attend and/or donate to the cause! Though our logo colors are blue/green/burgandy, this can use black/gold/silver/white as well. Our website is www.hcalorvin.org if that helps explain who we are.

Also, it can be abstract. And it does not have to include ballroom dancers if the word mark or other graphics are eye catching.

Target Market(s)

Donors, upscale, higher income,45-70, men and women (though women will more likely make the decision to attend)

Industry/Entity Type

Tv

Requirements
Must have
• The wording to be incorporated into the invitation cover is:
Harborview Community Aid
Celebrates Stepping Up for Decades with
Twirl Under Moonbeams
hosted by Host Name (will give the final name when confirmed)

Saturday, November 8, 2014
7 pm
Marlowe Cincinnati Crestwood Tower
Nice to have
• I'd like to see something other than ballroom dancers just to give my committee some options. Is it possible to show footprints of dancers (man's shoe with woman's high heels) as the design element? Something that can be used across the invite (rsvp card).
Should not have
• You have free range to create and have fun! If you use our logo colors, either choose one color as the focus, or just be sure to focus on green and burgandy together

```html
<!DOCTYPE html>
<html lang="en">
<head>
<meta charset="utf-8">
<title>Harborview Community Aid – Twirl Under Moonbeams</title>
<link rel="stylesheet" href="https://fonts.googleapis.com/css2?family=Archivo+Black&family=Cinzel:wght@700;900&family=Fjalla+One&family=Nunito:wght@600&display=swap">
<style>
  :root{
    --sheet:#eceeee;
    --ink:#2b2b2f;
    --white:#ffffff;
    --cream:#fff6d8;
    --gold-light:#fbe7a1;
    --gold:#e2b53c;
    --gold-deep:#a97a12;
    --silver:#e6e6ea;
    --ray-blue:#2a2fd0;
    --ray-violet:#6a2bb8;
    --ray-red:#9a1c3c;
    --ray-teal:#1d7f8f;
  }
  *{margin:0;padding:0;box-sizing:border-box}
  html,body{width:1200px;height:884px;overflow:hidden;background:var(--sheet)}
  .sheet{position:relative;width:1200px;height:884px;background:var(--sheet)}

  .cover{position:absolute;top:47px;height:812px;background:var(--ink);overflow:hidden;
    font-family:"Fjalla One",sans-serif;color:var(--white)}
  .cover--foil{left:18px;width:575px}
  .cover--classic{left:606px;width:577px;height:813px}

  .cover__rays{position:absolute;left:0;top:60px;width:100%;height:700px;
    background:
      radial-gradient(ellipse 60% 28% at 30% 45%, rgba(120,200,255,.35), transparent 70%),
      radial-gradient(ellipse 40% 25% at 20% 12%, var(--ray-red), transparent 75%),
      radial-gradient(ellipse 45% 30% at 85% 70%, var(--ray-teal), transparent 75%),
      radial-gradient(ellipse 70% 45% at 45% 50%, var(--ray-blue), transparent 80%),
      radial-gradient(ellipse 90% 55% at 60% 55%, var(--ray-violet), transparent 85%);
    opacity:.95}
  .cover__rays::after{content:"";position:absolute;inset:0;
    background:linear-gradient(180deg,var(--ink) 0%,transparent 18%,transparent 82%,var(--ink) 100%)}

  .brand{position:absolute;top:42px;display:flex;align-items:center;gap:10px;
    font-family:"Nunito",sans-serif;font-weight:600;font-size:18px;color:var(--white);white-space:nowrap}
  .brand__dot{width:30px;height:30px;border-radius:50%;background:var(--white)}
  .cover--foil .brand{left:155px}
  .cover--classic .brand{left:55px}

  .tagline{position:absolute;top:127px;font-size:23px;letter-spacing:.2px;white-space:nowrap;text-transform:uppercase}
  .cover--foil .tagline{left:69px}
  .cover--classic .tagline{left:68px}

  .gold{background:linear-gradient(180deg,var(--gold-light) 0%,var(--gold) 45%,var(--gold-deep) 60%,var(--gold-light) 100%);
    -webkit-background-clip:text;background-clip:text;color:transparent}

  .title{position:absolute;line-height:1;white-space:nowrap}
  .title--foil{font-family:"Archivo Black",sans-serif;left:70px;top:162px}
  .title--foil .title__main{display:block;font-size:104px;letter-spacing:2px}
  .title--foil .title__line{display:block;margin-top:-2px}
  .title--foil .title__small{font-size:28px;margin-right:8px}
  .title--foil .title__end{font-size:44px}

  .title--classic{font-family:"Cinzel",serif;font-weight:900;left:64px;top:172px}
  .title--classic .title__main{display:block;font-size:84px}
  .title--classic .title__small{display:block;font-size:34px;margin:6px 0 0 10px;font-weight:700}
  .title--classic .title__end{display:block;font-size:54px;margin-top:2px}

  .star{position:absolute;fill:none;stroke:var(--gold);stroke-width:4;stroke-linejoin:miter}

  .dancers{position:absolute;border-radius:45% 45% 40% 40%}
  .cover--foil .dancers{left:265px;top:360px;width:260px;height:400px;
    background:radial-gradient(ellipse 50% 50% at 50% 50%, rgba(226,181,60,.85) 0%, rgba(226,181,60,.55) 45%, rgba(169,122,18,0) 100%)}
  .cover--classic .dancers{left:250px;top:362px;width:265px;height:380px;
    background:
      radial-gradient(ellipse 35% 45% at 35% 45%, rgba(230,230,234,.8), rgba(230,230,234,0) 100%),
      radial-gradient(ellipse 50% 50% at 60% 55%, rgba(226,181,60,.85) 0%, rgba(226,181,60,.5) 50%, rgba(169,122,18,0) 100%)}

  .event{position:absolute;top:548px;font-size:15px;line-height:22px;text-align:center;color:var(--cream)}
  .cover--foil .event{left:47px;width:240px}
  .cover--classic .event{left:40px;width:240px}

  .host{position:absolute;top:746px;font-size:15px;color:var(--white)}
  .cover--foil .host{left:58px}
  .cover--classic .host{left:57px}
</style>
</head>
<body>
<main class="sheet">

  <section class="cover cover--foil">
    <div class="cover__rays" role="img" aria-label="Abstract light rays in blue, violet and red"></div>
    <div class="brand"><span class="brand__dot"></span>Harborview Community Aid</div>
    <p class="tagline">Celebrates Stepping Up for Decades with</p>
    <h1 class="title title--foil">
      <span class="title__main gold">twirl</span>
      <span class="title__line"><span class="title__small gold">under our</span><span class="title__end gold">moonbeams</span></span>
    </h1>
    <svg class="star" style="left:502px;top:232px" width="44" height="42" viewBox="0 0 44 42" aria-hidden="true"><polygon points="22,3 27,16 41,16 30,25 34,39 22,31 10,39 14,25 3,16 17,16"/></svg>
    <svg class="star" style="left:127px;top:358px" width="64" height="62" viewBox="0 0 44 42" aria-hidden="true"><polygon points="22,3 27,16 41,16 30,25 34,39 22,31 10,39 14,25 3,16 17,16"/></svg>
    <div class="dancers" role="img" aria-label="Gold foil silhouette of a ballroom dancing couple"></div>
    <p class="event">Saturday, November 8, 2014<br>7 pm<br>Marlowe Cincinnati Crestwood Tower</p>
    <p class="host">hosted by Host Name</p>
  </section>

  <section class="cover cover--classic">
    <div class="cover__rays" role="img" aria-label="Abstract light rays in blue, violet and red"></div>
    <div class="brand"><span class="brand__dot"></span>Harborview Community Aid</div>
    <svg class="star" style="left:470px;top:38px" width="66" height="64" viewBox="0 0 44 42" aria-hidden="true"><polygon points="22,3 27,16 41,16 30,25 34,39 22,31 10,39 14,25 3,16 17,16"/></svg>
    <p class="tagline">Celebrates Stepping Up for Decades with</p>
    <h1 class="title title--classic">
      <span class="title__main gold">TWIRL</span>
      <span class="title__small gold">UNDER OUR</span>
      <span class="title__end gold">MOONBEAMS</span>
    </h1>
    <svg class="star" style="left:318px;top:252px" width="46" height="44" viewBox="0 0 44 42" aria-hidden="true"><polygon points="22,3 27,16 41,16 30,25 34,39 22,31 10,39 14,25 3,16 17,16"/></svg>
    <svg class="star" style="left:152px;top:426px" width="44" height="42" viewBox="0 0 44 42" aria-hidden="true"><polygon points="22,3 27,16 41,16 30,25 34,39 22,31 10,39 14,25 3,16 17,16"/></svg>
    <div class="dancers" role="img" aria-label="Silver and gold silhouette of a ballroom dancing couple"></div>
    <p class="event">Saturday, November 8, 2014<br>7 pm<br>Marlowe Cincinnati Crestwood Tower</p>
    <p class="host">hosted by Host Name</p>
  </section>

</main>
</body>
</html>
```